Redesign Tea Boxes

Redesign teas boxes to make them more vibrant and modern. Maintaining the Brand Heritage. We find that our teaboxes are outdated and do not stand the t

Target Market(s)

Trendy women living in Cities. Ages 24 - 45
They are very upwardly mobile and know their Social Media: On Chatterly, Pixelwave, and quipdrop
They are into investing.
They take their kids to what they consider good public schools but most of them take their kids to private schools
38% are taking Masters Classes or Certificate Classes that will advance them getting better pay at work.
Likes to go coffee shops, malls, bars, and clubs

Requirements
Must have
• Must maintain vibrant attractive colors. Health Benefits. Logo with the yellow band at the top.
Nice to have
• The leaves

```html
<!DOCTYPE html>
<html lang="en">
<head>
<meta charset="utf-8">
<title>Maple's FreshLeaf Green Tea – Box Dieline</title>
<link rel="stylesheet" href="https://fonts.googleapis.com/css2?family=Fira+Sans:wght@400;700;800&family=Kaushan+Script&display=swap">
<style>
  :root{
    --lime:#b4e01a;
    --lime-deep:#6fb514;
    --leaf:#3f8d12;
    --text-green:#4e9a0c;
    --orange:#f08a4b;
    --orange-soft:#f6a56f;
    --gold-line:#efd391;
    --cut:#1d1d1d;
    --paper:#ffffff;
    --sans:"Fira Sans", Arial, sans-serif;
    --script:"Kaushan Script", cursive;
  }
  *{box-sizing:border-box;margin:0;padding:0}
  html,body{width:1200px;height:1200px;overflow:hidden;background:var(--paper)}
  .stage{position:absolute;left:0;top:0;width:1000px;height:1000px;transform:scale(1.2);transform-origin:0 0;font-family:var(--sans)}
  .dieline{position:absolute;left:0;top:0;width:1000px;height:1000px}
  .panel{position:absolute;overflow:hidden;border:0.8px solid var(--cut);background:var(--paper)}

  /* ---------- front face ---------- */
  .front{width:273px;height:152px}
  .front-art{position:absolute;inset:0;width:100%;height:100%}
  .front-illustration{position:absolute;left:100px;top:14px;width:150px;height:118px;border-radius:50%;
    background:radial-gradient(ellipse at 55% 50%, #7fff3a 0%, #b9f07a 35%, rgba(235,250,220,.85) 60%, rgba(255,255,255,0) 75%)}
  .brand{position:absolute;left:12px;top:12px;color:var(--leaf);font-weight:700;line-height:1;display:flex;align-items:center;gap:3px}
  .brand-dot{width:6px;height:6px;border-radius:50%;background:var(--leaf)}
  .brand-name{display:flex;flex-direction:column}
  .brand-name small{font-size:5px}
  .brand-name span{font-size:11px}
  .bag-count{position:absolute;right:6px;top:4px;font-size:6.5px;font-weight:800;color:#fff;letter-spacing:.2px;white-space:nowrap}
  .organic{position:absolute;left:26px;top:108px;background:var(--orange);color:#fff;font-size:5.5px;font-weight:700;padding:1px 6px;border-radius:6px;letter-spacing:.4px;line-height:1.2;white-space:nowrap}
  .product-name{position:absolute;left:10px;top:118px;font-family:var(--script);font-size:21px;line-height:1.2;color:var(--leaf);white-space:nowrap}
  .tagline-band{position:absolute;right:0;bottom:0;width:113px;height:22px;background:var(--orange-soft);border-radius:10px 0 0 0;
    display:flex;align-items:center;justify-content:center;font-family:var(--script);font-size:7.5px;color:#fff;white-space:nowrap}

  /* ---------- rotated front (bottom face) ---------- */
  .front-rot{width:273px;height:157px}
  .rot-inner{position:absolute;left:50%;top:50%;width:157px;height:273px;transform:translate(-50%,-50%) rotate(90deg)}
  .rot-inner .brand{left:12px;top:14px}
  .rot-inner .bag-count{color:var(--leaf);right:6px;top:6px}
  .rot-illustration{position:absolute;left:0;bottom:22px;width:125px;height:100px;border-radius:50%;
    background:radial-gradient(ellipse at 50% 50%, #7fff3a 0%, #b9f07a 35%, rgba(235,250,220,.85) 60%, rgba(255,255,255,0) 75%)}
  .rot-inner .organic{left:94px;top:98px}
  .rot-inner .product-name{left:40px;top:110px;font-size:24px;line-height:1.2}
  .net-weight{position:absolute;left:122px;top:76px;font-size:9px;font-weight:800;color:var(--leaf);white-space:nowrap}
  .rot-inner .tagline-band{width:100%;border-radius:0;height:20px}

  /* ---------- side panels ---------- */
  .side{width:157px;height:138px}
  .side-inner{position:absolute;left:50%;top:50%;width:138px;height:157px;color:var(--text-green);font-weight:700}
  .side-left .side-inner{transform:translate(-50%,-50%) rotate(-90deg)}
  .side-right .side-inner{transform:translate(-50%,-50%) rotate(90deg)}
  .side-strip{position:absolute;left:0;bottom:0;width:100%;height:20px;background:linear-gradient(180deg,#fff 0%,var(--lime) 60%,var(--lime-deep) 100%);
    display:flex;justify-content:space-between;align-items:flex-start;padding:2px 8px;font-size:6px;font-weight:800;color:var(--leaf)}
  .side-copy{padding:10px 10px 0 12px;font-size:6px;line-height:1.35}
  .side-copy h3{font-size:6.5px;font-weight:800;margin-bottom:4px}
  .side-copy ul{list-style:none}
  .side-copy p{margin-top:5px}
  .side-copy .storage{margin-top:6px;font-weight:800;letter-spacing:.2px}

  /* ---------- back panel ---------- */
  .back{width:273px;height:138px;padding:10px 8px 0 10px;color:var(--text-green);font-size:6.2px;font-weight:700;line-height:1.32}
  .back .contact{margin-top:3px}
</style>
</head>
<body>
<div class="stage">

  <svg class="dieline" viewBox="0 0 1000 1000" aria-hidden="true">
    <g fill="#fff" stroke="var(--cut)" stroke-width="0.8">
      <path d="M352,200 L312,210 L310,342 L352,352 Z"/>
      <path d="M625,200 L665,210 L667,342 L625,352 Z"/>
      <path d="M195,355 L166,355 Q150,358 150,374 L150,476 Q150,490 166,493 L195,493 Z"/>
      <path d="M782,355 L811,355 Q826,358 826,374 L826,476 Q826,490 811,493 L782,493 Z"/>
      <path d="M352,496 L312,506 L310,640 L352,650 Z"/>
      <path d="M625,496 L665,506 L667,640 L625,650 Z"/>
      <path d="M352,787 L352,800 Q355,815 375,815 L602,815 Q624,815 625,800 L625,787"/>
    </g>
    <line x1="345" y1="190" x2="632" y2="190" stroke="var(--gold-line)" stroke-width="1.2"/>
  </svg>

  <!-- Front face (top) -->
  <section class="panel front" style="left:352px;top:200px">
    <svg class="front-art" viewBox="0 0 273 152" preserveAspectRatio="none" aria-hidden="true">
      <defs>
        <linearGradient id="frontBg" x1="0" y1="0" x2="1" y2="1">
          <stop offset="0" stop-color="#c7ec2a"/><stop offset=".6" stop-color="#8fcc14"/><stop offset="1" stop-color="#5ea812"/>
        </linearGradient>
      </defs>
      <rect width="273" height="152" fill="url(#frontBg)"/>
      <path d="M0,80 Q70,50 130,70 L130,152 L0,152 Z" fill="#fff"/>
      <path d="M0,76 Q60,44 150,58" fill="none" stroke="var(--orange)" stroke-width="3"/>
      <path d="M0,70 Q60,38 150,50" fill="none" stroke="#f5d23a" stroke-width="2"/>
    </svg>
    <div class="front-illustration" role="img" aria-label="Glass cup of green tea on a saucer with fresh tea leaves"></div>
    <div class="brand"><span class="brand-dot"></span><span class="brand-name"><small>Maple's</small><span>FreshLeaf</span></span></div>
    <div class="bag-count">25 TEA BAGS</div>
    <div class="organic">ORGANIC</div>
    <div class="product-name">Green Tea</div>
    <div class="tagline-band">Take Life The FreshLeaf Way</div>
  </section>

  <!-- Left side panel: benefits -->
  <section class="panel side side-left" style="left:195px;top:355px">
    <div class="side-inner">
      <div class="side-copy">
        <h3>Benefits</h3>
        <ul>
          <li>&gt;Lorem ipsum dolor sit amet, at dolor ornatus.</li>
          <li>&gt;Lorem ipsum dolor sit amet, at dolor ornatus.</li>
          <li>&gt;Lorem ipsum dolor sit amet, at dolor ornatus.</li>
          <li>&gt;Lorem ipsum dolor sit amet, at dolor ornatus.</li>
          <li>&gt;Lorem ipsum dolor sit amet, at dolor ornatus.</li>
        </ul>
      </div>
      <div class="side-strip"><span>25 TEA BAGS</span><span>50g</span></div>
    </div>
  </section>

  <!-- Back panel -->
  <section class="panel back" style="left:352px;top:355px">
    <p>Lorem ipsum dolor sit amet, sed at simul alitr fierent. Movet choro mei te, ubique imperdiet mediocritatem cu vel. No elit numquam ius, liber iuvaret consequuntur ad cum, cu scripserit adversarium nec. Ius decore facilis te, alia impedit dignissim eu usu. Animal mentitum ea pro, in malis oportere honestatis sed. Est at saepe veniam, decore minimum hendrerit duo eu.</p>
    <p>Vel cu dolorem aliquando referrentur, copiosae placerat sententiae te pri. Pri tractatos iudicabit ex, decore gubergren evertitur nam an. Ex eirmod commodo ius, cu fugit error pri, vim ne cibo oratio accusamus. Ex pri tantas alienum philosophia, cu cum utamur sensibus, ipsum feugait quaestio eos cu.</p>
    <p class="contact">Lorem ipsum dolor sit.<br>Lorem ipsum dolor sit.<br>Lorem ipsum dolor sit.<br>Lorem ipsum dolor sit.<br>www.</p>
  </section>

  <!-- Right side panel: preparation -->
  <section class="panel side side-right" style="left:625px;top:355px">
    <div class="side-inner">
      <div class="side-copy">
        <h3>Preparation suggestions</h3>
        <ul>
          <li>&gt;Steep 1 bag in 250ml freshly boiled water for 3-5 minutes</li>
          <li>&gt;Drink hot or cold</li>
          <li>&gt;Use Maple's FreshLeaf Honey to sweeten</li>
        </ul>
        <p>No chemicals, additives or preservatives</p>
        <p class="storage">STORE IN COOL DRY PLACE</p>
      </div>
      <div class="side-strip"><span>25 TEA BAGS</span><span>50g</span></div>
    </div>
  </section>

  <!-- Bottom face (rotated front) -->
  <section class="panel front-rot" style="left:352px;top:493px">
    <div class="rot-inner">
      <svg class="front-art" viewBox="0 0 157 273" preserveAspectRatio="none" aria-hidden="true">
        <defs>
          <linearGradient id="rotBg" x1="0" y1="0" x2="1" y2="1">
            <stop offset="0" stop-color="#c7ec2a"/><stop offset=".6" stop-color="#8fcc14"/><stop offset="1" stop-color="#5ea812"/>
          </linearGradient>
        </defs>
        <rect width="157" height="273" fill="url(#rotBg)"/>
        <path d="M0,0 L80,0 Q60,90 0,120 Z" fill="#fff"/>
        <path d="M85,0 Q70,90 0,128" fill="none" stroke="var(--orange)" stroke-width="3"/>
        <path d="M95,0 Q80,100 0,140" fill="none" stroke="#f5d23a" stroke-width="2"/>
        <path d="M0,150 Q60,150 157,180 L157,273 L0,273 Z" fill="#fff"/>
      </svg>
      <div class="rot-illustration" role="img" aria-label="Glass cup of green tea on a saucer with fresh tea leaves"></div>
      <div class="brand"><span class="brand-dot"></span><span class="brand-name"><small>Maple's</small><span>FreshLeaf</span></span></div>
      <div class="bag-count">25 TEA BAGS</div>
      <div class="net-weight">50 g.</div>
      <div class="organic">ORGANIC</div>
      <div class="product-name">Green Tea</div>
      <div class="tagline-band">Take Life The FreshLeaf Way</div>
    </div>
  </section>

  <!-- Front face (second) -->
  <section class="panel front" style="left:352px;top:650px;height:137px">
    <svg class="front-art" viewBox="0 0 273 137" preserveAspectRatio="none" aria-hidden="true">
      <defs>
        <linearGradient id="frontBg2" x1="0" y1="0" x2="1" y2="1">
          <stop offset="0" stop-color="#c7ec2a"/><stop offset=".6" stop-color="#8fcc14"/><stop offset="1" stop-color="#5ea812"/>
        </linearGradient>
      </defs>
      <rect width="273" height="137" fill="url(#frontBg2)"/>
      <path d="M0,72 Q70,45 130,62 L130,137 L0,137 Z" fill="#fff"/>
      <path d="M0,68 Q60,40 150,52" fill="none" stroke="var(--orange)" stroke-width="3"/>
      <path d="M0,62 Q60,34 150,44" fill="none" stroke="#f5d23a" stroke-width="2"/>
    </svg>
    <div class="front-illustration" role="img" aria-label="Glass cup of green tea on a saucer with fresh tea leaves" style="height:110px;top:12px"></div>
    <div class="brand"><span class="brand-dot"></span><span class="brand-name"><small>Maple's</small><span>FreshLeaf</span></span></div>
    <div class="bag-count">25 TEA BAGS</div>
    <div class="organic" style="top:80px">ORGANIC</div>
    <div class="product-name" style="top:92px">Green Tea</div>
    <div class="tagline-band">Take Life The FreshLeaf Way</div>
  </section>

</div>
</body>
</html>
```